Stationery Design

Need a stationery design for an established accounting firm based in London, England.

The company’s name is ‘Harold Brinkley’. We provide a broad range of bookkeeping, accounting, audit, tax and business services to a wide range of clients (ie, individuals, company, partnerships, etc).

The stationary design needs to show strength and trust and should be clean, corporate and professional.

Only 2 colours must be used as noted on the logo.

The fonts are in Optima

We need the following:

#1: Business Cards (design on 2 sides)
#2: Letterhead (word format) and can be sent to printers
#3: Continuation sheets (word format) and can be sent to printers
#4: Sales invoice template (word format) and can be sent to printers
#5: Report Cover front and back for binding,
#6: Complimentary Slips,
#7: Legal corners with our logo only
#7: Email signature templates

I have attached my company's logo in various file formats

We also need to have our accountancy association’s logo and this must be in the same colour as the dark blue. This PQTB logo must be at least 8mm square (can be larger). I have attached the PQTB logo in various file formats

I have also attached other information that you will need for the letter head and invoice templates

I have also attached our old letterhead, fee note template for reference
Updates

Dear Designers - I have increased the budget

Dear Designers - I have read your comments on the fact that the prize does not reflect the work. Thank you and I appreciate your comments. Unfortunately, I am a start up and my budget is limited. As an Alternative, I have reduced the work that I am asking for to the following items and I hope you can assist: #1: Business Cards (design on 2 sides) #2: Letterhead (word format) and can be sent to printers #3: Report Cover front and back for binding, #4: Email signature templates Regards

Industry/Entity Type

Accounting

```html
<!DOCTYPE html>
<html lang="en">
<head>
<meta charset="utf-8">
<title>Harold Brinkley – Email Signature</title>
<link rel="stylesheet" href="https://fonts.googleapis.com/css2?family=Source+Sans+3:ital,wght@0,400;0,600;0,700;1,400&display=swap">
<style>
  :root {
    --navy: #1f3561;
    --plum: #7b1c5c;
    --rule: #9aa1ad;
    --paper: #ffffff;
  }
  * { box-sizing: border-box; margin: 0; padding: 0; }
  html, body {
    width: 1200px; height: 1000px; overflow: hidden;
    background: var(--paper);
  }
  body {
    font-family: "Source Sans 3", sans-serif;
    color: var(--navy);
  }
  .signature {
    position: absolute; left: 70px; top: 235px; width: 1060px;
  }
  .signature__name {
    font-size: 33px; font-weight: 400; letter-spacing: 0.2px; line-height: 1;
    margin-left: 3px;
  }
  .signature__name em { font-size: 27px; font-style: italic; margin-left: 4px; }
  .brand {
    display: flex; align-items: center; gap: 14px;
    margin: 26px 0 0 3px; height: 54px;
  }
  .brand__square {
    width: 40px; height: 40px; background: var(--plum);
  }
  .brand__name {
    font-size: 31px; font-weight: 400; letter-spacing: 1px; color: var(--navy);
  }
  .signature__rule {
    height: 2px; background: var(--rule); margin-top: 25px;
  }
  .contact {
    display: grid; grid-template-columns: 352px 314px 390px;
    margin: 14px 0 0 11px; font-size: 14.5px; line-height: 21px;
  }
  .contact__regulation { text-align: justify; }
  .company-line {
    margin: 20px 0 0 11px; font-size: 16px; font-weight: 700; line-height: 22px;
  }
  .notice { margin: 24px 0 0 11px; }
  .notice__title {
    display: inline-block; font-size: 20px; font-weight: 700;
    border-bottom: 2px solid var(--navy); line-height: 22px; margin-bottom: 12px;
  }
  .notice__text {
    font-size: 15.5px; font-style: italic; line-height: 19.5px;
    width: 1040px; margin-bottom: 19px;
  }
</style>
</head>
<body>
  <section class="signature">
    <h1 class="signature__name">Marcus Ellery <em>FPQTB</em></h1>

    <div class="brand">
      <span class="brand__square" aria-hidden="true"></span>
      <span class="brand__name">HAROLD BRINKLEY</span>
    </div>

    <div class="signature__rule"></div>

    <div class="contact">
      <address class="contact__address" style="font-style:normal">
        12 Fenwick Court,<br>
        Kingsmere Business Park,<br>
        Aldridge Road, Northgate-on-the-Hill,<br>
        Middlesex NG4 7PL
      </address>
      <p class="contact__lines">
        T: 0208 555 0142<br>
        M: 07700 900 318<br>
        E: marcus@haroldbrinkley.co.uk<br>
        W: www.haroldbrinkley.co.uk
      </p>
      <p class="contact__regulation">
        Registered as auditors and regulated for a range of business activities in the United Kingdom by the Association of Professional Qualified Tax Bookkeepers.
      </p>
    </div>

    <p class="company-line">
      Harold Brinkley is a trading name of Harold Brinkley Limited, a company registered in England and Wales, (Registration number 09817362)<br>
      whose registered office is at 12 Fenwick Court, Kingsmere Business Park, Aldridge Road, Northgate-on-the-Hill, NG4 7PL.
    </p>

    <div class="notice">
      <h2 class="notice__title">IMPORTANT NOTICE</h2>
      <p class="notice__text">This communication and any attachments are confidential and may be protected from disclosure. We endorse no information, opinion or advice contained in this communication that is not the subject of a contract between the recipient and us. If you have received it in error please notify us immediately and note that any storage, use or disclosure is strictly prohibited and may be unlawful.</p>
      <p class="notice__text">Whilst we check the communications we send for virus infection, we accept no responsibility for any loss or damage caused to your systems by this communication.</p>
      <p class="notice__text">Those communicating with us by electronic mail will be deemed to have accepted the risks associated with interception, amendment, loss and late or incomplete delivery. They will also be deemed to have consented to our intercepting and monitoring such communications.</p>
    </div>
  </section>
</body>
</html>
```